Business Card & Email Signature Design || Upmarket + Luxury

Riverlume Honey, a New Zealand Manuka Honey company needs a Business Card & Email Signature design.

Our logo's are attached in Gold & Black versions, feel free to be creative with how you use the logo and it's patterns in your design.

Style:
- Looking for an Elegant, Luxurious, Upmarket feel.
- Black/Matte Black Card, Gold Foil, UV Embossing

Information to Add:

- Logo
- Company Name: Riverlume Honey
- Name: Mattias Brovell
- Title: Creative Director
- Phone: +64 2919 58 617
- Email: mattias@riverlumehoney.example
- Website: www.riverlumehoney.example

- Socials: ***For email Signature Only***
- Facebook: https://www.facebook.com/riverlumehoney/
- Instagram: https://www.instagram.com/riverlumehoney/

Target Market(s)

Asia/Europe Luxury, Upmarket

Contact Information for Business Card

- Logo
- Name: Mattias Brovell
- Phone: +64 2919 58 617

Font styles to use
Other font styles liked:
• Champagne & Limousines (Attached)

Requirements
Must have
• Business Card & Email Signature Design.

Looking for a Sleek, Luxury, Upmarket Design.

```html
<!DOCTYPE html>
<html lang="en">
<head>
<meta charset="utf-8">
<title>Riverlume Honey — Business Card</title>
<link href="https://fonts.googleapis.com/css2?family=Josefin+Sans:wght@300;400;600&display=swap" rel="stylesheet">
<style>
  :root {
    --page: #ffffff;
    --card: #2b2b2c;
    --card-edge: #242425;
    --gold: #d9b04a;
    --gold-light: #f0cf72;
    --gold-deep: #a9822a;
    --ink-on-gold: #2a2212;
  }
  * { box-sizing: border-box; margin: 0; padding: 0; }
  html, body { width: 1200px; height: 426px; overflow: hidden; background: var(--page); }
  body { position: relative; font-family: "Josefin Sans", sans-serif; }

  .card {
    position: absolute;
    top: 61px;
    width: 494px;
    height: 283px;
    background: linear-gradient(160deg, #323233 0%, var(--card) 45%, var(--card-edge) 100%);
    overflow: hidden;
  }
  .card--front { left: 50px; }
  .card--back { left: 642px; }

  /* Front */
  .brand-lockup {
    position: absolute;
    left: 0; right: 0; top: 104px;
    display: flex; align-items: center; justify-content: center; gap: 12px;
  }
  .brand-lockup__dot {
    width: 10px; height: 10px; border-radius: 50%; background: var(--gold);
  }
  .brand-lockup__name {
    color: var(--gold);
    font-size: 22px; font-weight: 400; letter-spacing: 5px; text-transform: uppercase;
  }
  .web-band {
    position: absolute; left: 0; right: 0; top: 221px; height: 25px;
    background: linear-gradient(90deg, var(--gold-deep), var(--gold) 30%, var(--gold-light) 55%, var(--gold) 80%, var(--gold-deep));
    display: flex; align-items: center; justify-content: center;
  }
  .web-band__url {
    color: var(--ink-on-gold);
    font-size: 12px; font-weight: 400; letter-spacing: 4px; text-transform: uppercase;
    padding-top: 2px;
  }

  /* Back */
  .company-name {
    position: absolute; right: 16px; top: 19px;
    color: var(--gold); font-size: 15px; font-weight: 400; letter-spacing: 3px;
  }
  .ribbon { position: absolute; left: 54px; top: 0; width: 27px; height: 103px; }
  .person { position: absolute; left: 92px; top: 60px; }
  .person__name { color: var(--gold); font-size: 29px; font-weight: 300; line-height: 1; }
  .person__name strong { font-weight: 400; }
  .person__title { color: var(--gold); font-size: 12px; font-weight: 300; margin-top: 6px; }

  .contact { position: absolute; left: 0; top: 0; width: 100%; height: 100%; }
  .contact__icon { position: absolute; width: 28px; height: 32px; }
  .contact__text {
    position: absolute; left: 92px;
    color: var(--gold); font-size: 14px; font-weight: 400; line-height: 1;
  }
</style>
</head>
<body>

<section class="card card--front">
  <div class="brand-lockup">
    <span class="brand-lockup__dot"></span>
    <span class="brand-lockup__name">Riverlume Honey</span>
  </div>
  <div class="web-band">
    <span class="web-band__url">www.riverlumehoney.example</span>
  </div>
</section>

<section class="card card--back">
  <p class="company-name">RIVERLUME HONEY</p>

  <svg class="ribbon" viewBox="0 0 27 103" aria-hidden="true">
    <defs>
      <linearGradient id="ribbonGold" x1="0" x2="1">
        <stop offset="0" stop-color="#a9822a"/>
        <stop offset="0.5" stop-color="#f0cf72"/>
        <stop offset="1" stop-color="#b58d30"/>
      </linearGradient>
    </defs>
    <path d="M0 0H27V96L13.5 103L0 96Z" fill="url(#ribbonGold)"/>
    <circle cx="13.5" cy="67" r="5" fill="#2b2b2c"/>
    <path d="M5 86a8.5 8 0 0 1 17 0Z" fill="#2b2b2c"/>
  </svg>

  <div class="person">
    <p class="person__name"><strong>Mattias</strong> Brovell</p>
    <p class="person__title">Creative Director</p>
  </div>

  <div class="contact">
    <svg class="contact__icon" style="left:40px;top:142px" viewBox="0 0 28 32" aria-hidden="true">
      <path d="M14 1.5L26.5 8.5V23.5L14 30.5L1.5 23.5V8.5Z" fill="none" stroke="#d9b04a" stroke-width="1.5"/>
      <path d="M10 10c1.5-1 2.5 0 3 1.5l-1.2 1.5c.6 1.6 1.8 3 3.4 3.8l1.5-1.1c1.5.6 2.3 1.6 1.3 3.1-1 1.3-3 1.4-5-.2-2.2-1.7-3.9-4-4.4-6.4-.3-1.1.3-1.8 1.4-2.2Z" fill="#d9b04a"/>
    </svg>
    <p class="contact__text" style="top:152px">+64 2919 58 617</p>

    <svg class="contact__icon" style="left:53px;top:173px" viewBox="0 0 28 32" aria-hidden="true">
      <path d="M14 1.5L26.5 8.5V23.5L14 30.5L1.5 23.5V8.5Z" fill="none" stroke="#d9b04a" stroke-width="1.5"/>
      <rect x="7" y="11" width="14" height="10" fill="#d9b04a"/>
      <path d="M7 11L14 17L21 11M7 21L12 16M21 21L16 16" fill="none" stroke="#2b2b2c" stroke-width="1"/>
    </svg>
    <p class="contact__text" style="top:183px">mattias@riverlumehoney.example</p>

    <svg class="contact__icon" style="left:40px;top:203px" viewBox="0 0 28 32" aria-hidden="true">
      <path d="M14 1.5L26.5 8.5V23.5L14 30.5L1.5 23.5V8.5Z" fill="none" stroke="#d9b04a" stroke-width="1.5"/>
      <g fill="none" stroke="#d9b04a" stroke-width="1.2">
        <circle cx="14" cy="16" r="7"/>
        <ellipse cx="14" cy="16" rx="3" ry="7"/>
        <path d="M7 16H21M8.2 12.5H19.8M8.2 19.5H19.8"/>
      </g>
    </svg>
    <p class="contact__text" style="top:213px">mattias@riverlumehoney.example</p>
  </div>
</section>

</body>
</html>
```